TotHaven Community Landing Page

TotHaven is a virtual world built with childrens' needs in mind. It is an online portal where parents will find all kids' related stuffs and a community connect point for parents to interact and share their experiences.

We need the designs for 2 pages within TotHaven:
- Landing Page for the Community Area
- Registration page for membership

1) The Landing Page need to have the following:

Logo & Main Background :- use the images attached

Page Title & Navigation Menu :-
The page title is "Community Connect"; navigation menu should be able to hold at least 6 tabs

Login Widget* :-
We want to put emphasis on the design of this.
For visitors, this is a normal login widget with username/password input fields, register button and 'login with chatterbook' button.
For logged-in users, this becomes a simple dashboard widget with Avatar, shortlinks and some useful navigation buttons.

"Groups" Section :-
This area holds an image, a short paragraph introducing "Groups", a widget showing 5-10 latest/popular groups and a 'Go to Groups' button at the bottom.

"Forum" Section :-
This area holds an image, a short paragraph introducing "Forum", a widget showing 5-10 latest/popular discussion topics and a 'Go to Forum' button at the bottom.

"Activities" Section -
This area holds an image, a short paragraph introducing "Forum", a widget showing 5-10 latest/popular events & activities and a 'Go to Activities' button at the bottom.

"Marketplace" Section :-
This area holds an image, a short paragraph introducing "Marketplace", a widget showing 5-10 latest/popular products and a 'Go to Marketplace' button at the bottom.

Social Media elements :-
The usual social media icons and chatterbook like box.

2) The Registration Page will need to contain the registration form as per the image attached.

Target Market(s)

Parents with kids ranging from 2 - 12 years old

Industry/Entity Type

Events

Requirements
Nice to have
• - colorful illustrations of kids or kids related images all around

```html
<!DOCTYPE html>
<html lang="en">
<head>
<meta charset="utf-8">
<title>TotHaven – Community Connect</title>
<link href="https://fonts.googleapis.com/css2?family=Ubuntu:ital,wght@0,400;0,500;0,700;1,500&family=Open+Sans:wght@400;600&display=swap" rel="stylesheet">
<style>
:root{
  --sky-top:#7ccde6;
  --sky-mid:#2aa3dc;
  --grass:#6e9a24;
  --grass-dark:#557a18;
  --header-bg:#86d3e3;
  --page-bg:#f3f3ee;
  --card-bg:#ffffff;
  --card-border:#d9d9d2;
  --green:#6cbd2c;
  --green-dark:#4fa21d;
  --orange:#ff7d1c;
  --orange-dark:#f0600f;
  --red:#d0060e;
  --red-dark:#b10008;
  --purple:#b02ee8;
  --purple-dark:#9418cf;
  --nav-home:#b9403d;
  --nav-yellow:#f3d21a;
  --item-title:#a3192b;
  --text:#6a6a6a;
  --dark:#2d2d2d;
  --footer:#1ea6dc;
  --white:#ffffff;
}
*{box-sizing:border-box;margin:0;padding:0}
html,body{width:1200px;height:2214px;overflow:hidden}
body{position:relative;font-family:"Open Sans",sans-serif;color:var(--text);
  background:linear-gradient(180deg,var(--sky-top) 0,var(--sky-mid) 330px,#b9e3f3 520px,var(--grass) 700px,var(--grass) 1300px,var(--grass-dark) 2100px)}
.scenery{position:absolute;left:0;top:0;width:1200px;height:2106px}
.page{position:absolute;left:120px;top:0;width:960px;height:2106px;background:var(--page-bg);
  box-shadow:0 0 12px rgba(0,0,0,.25)}
/* header */
.site-header{position:absolute;left:10px;top:15px;width:939px;height:199px;background:var(--header-bg);border-radius:6px}
.brand{position:absolute;left:30px;top:60px;display:flex;align-items:center;gap:12px;
  font-family:"Ubuntu",sans-serif;font-weight:700;font-size:46px;color:var(--white)}
.brand-dot{width:34px;height:34px;border-radius:50%;background:#e8236f}
.login{position:absolute;left:596px;top:17px;width:340px;font-family:"Ubuntu",sans-serif}
.login-title{font-size:12px;font-weight:700;color:var(--dark);letter-spacing:.3px}
.login-fields{display:flex;gap:6px;margin-top:8px}
.login-fields span{width:164px;height:28px;background:var(--white);border-radius:3px;
  font-size:11px;font-style:italic;color:#b5b5b5;padding:7px 12px;box-shadow:inset 0 1px 3px rgba(0,0,0,.15)}
.login-row{display:flex;justify-content:flex-end;align-items:center;gap:10px;margin-top:7px;white-space:nowrap}
.forgot{font-size:11px;color:#2a6f9a}
.btn-register{background:#3b3b3b;color:var(--white);font-size:12px;font-weight:500;width:89px;height:28px;
  border-radius:3px;display:flex;align-items:center;justify-content:center}
.or{font-size:12px;font-weight:700;color:var(--dark)}
.btn-chatter{background:#3b5ba0;color:var(--white);font-size:11px;height:21px;width:149px;border-radius:2px;
  display:flex;align-items:center;gap:6px;padding-left:6px}
.btn-chatter i{width:12px;height:12px;background:var(--white);opacity:.9;border-radius:2px}
.main-nav{position:absolute;left:372px;top:152px;display:flex;gap:6px;font-family:"Ubuntu",sans-serif}
.main-nav a{height:29px;width:78px;display:flex;align-items:center;justify-content:center;font-size:13px;color:var(--white);
  white-space:nowrap;text-decoration:none;border:2px solid rgba(255,255,255,.55);border-radius:3px}
.nav-home{background:var(--nav-home)}.nav-groups{background:var(--green)}.nav-forums{background:var(--orange)}
.nav-activities{background:var(--red)}
.main-nav .nav-market{background:var(--purple);width:110px}
.main-nav .nav-contact{background:var(--nav-yellow);width:97px}
/* hero */
.hero{position:absolute;left:10px;top:223px;width:939px;height:378px;border-radius:6px;overflow:hidden;
  background:linear-gradient(120deg,#4f7a2a,#8fb25a 40%,#e9c9a8 55%,#5e8d2e)}
.hero-dots{position:absolute;right:12px;bottom:12px;display:flex;gap:6px}
.hero-dots i{width:19px;height:19px;border-radius:50%;background:rgba(255,255,255,.5)}
.hero-dots i:first-child{background:var(--white)}
/* sections */
.section{position:absolute;left:10px;width:939px;height:359px;background:var(--card-bg);
  border:2px solid var(--card-border);border-radius:6px}
.intro{position:absolute;left:9px;top:12px;width:288px;height:332px;border-radius:4px;padding:12px 14px 12px 12px;color:var(--white)}
.intro h2{font-family:"Ubuntu",sans-serif;font-weight:500;font-size:21px;letter-spacing:.3px}
.intro-photo{margin-top:8px;height:122px;border:3px solid var(--white)}
.intro p{margin-top:10px;font-size:12px;line-height:20px}
.latest{position:absolute;left:320px;top:10px;width:600px}
.latest h3{font-family:"Ubuntu",sans-serif;font-weight:500;font-size:18px}
.latest-grid{display:grid;grid-template-columns:290px 290px;column-gap:29px;margin-top:10px}
.item{height:92px;padding-top:4px;border-bottom:1px solid #e3e3e3}
.item:nth-last-child(-n+2){border-bottom:none}
.item h4{font-family:"Ubuntu",sans-serif;font-style:italic;font-weight:500;font-size:13.5px;color:var(--item-title);white-space:nowrap}
.item p{font-size:12px;line-height:18px;margin-top:3px}
.go{position:absolute;right:20px;bottom:12px;width:169px;height:33px;border-radius:3px;color:var(--white);
  font-family:"Ubuntu",sans-serif;font-weight:500;font-size:14px;display:flex;align-items:center;justify-content:center;white-space:nowrap}
.groups{top:618px}.forum{top:989px}.activities{top:1359px}.market{top:1730px}
.groups .intro{background:linear-gradient(180deg,#8ccf1c,var(--green-dark))}.groups h3{color:var(--green-dark)}
.groups .go{background:linear-gradient(180deg,#84cf3f,var(--green-dark))}
.groups .intro-photo{background:linear-gradient(180deg,#bfe3f5,#c99a6a 55%,#7fb247)}
.forum .intro{background:linear-gradient(180deg,#ff8c12,var(--orange-dark))}.forum h3{color:var(--orange-dark)}
.forum .go{background:linear-gradient(180deg,#ff9a35,var(--orange-dark))}
.forum .intro-photo{background:linear-gradient(135deg,#e0a77a,#4a8ec8 50%,#d9463b)}
.activities .intro{background:linear-gradient(180deg,var(--red),var(--red-dark))}.activities h3{color:var(--red-dark)}
.activities .go{background:linear-gradient(180deg,#e0171e,var(--red-dark))}
.activities .intro-photo{background:linear-gradient(135deg,#6a8fc4,#e7c7a6 50%,#d8b34a)}
.market .intro{background:linear-gradient(180deg,#c24bf0,var(--purple-dark))}.market h3{color:var(--purple-dark)}
.market .go{background:linear-gradient(180deg,#c04cf0,var(--purple-dark))}
.market .intro-photo{background:linear-gradient(135deg,#f3f3f3,#d95a3a 40%,#3a6fc4 70%,#f0d050)}
/* footer */
.site-footer{position:absolute;left:0;top:2106px;width:1200px;height:108px;background:var(--footer);color:var(--white)}
.footer-links{position:absolute;left:130px;top:27px;font-size:12px;white-space:nowrap}
.footer-links span{padding:0 6px;opacity:.8}
.copyright{position:absolute;left:130px;top:67px;font-size:10.5px}
.copyright b{color:var(--nav-yellow)}
.follow{position:absolute;right:134px;top:30px;display:flex;align-items:center;gap:10px;font-family:"Ubuntu",sans-serif;white-space:nowrap}
.follow-title{font-size:15px;margin-right:4px}
.social{display:flex;align-items:center;gap:5px;font-size:11px}
.social i{width:30px;height:30px;border-radius:50%;background:#2c3f8a;border:2px solid var(--white)}
.social.chirper i{background:#27a4dd}.social.feed i{background:#f26b21}.social.stream i{background:#d1241b}
</style>
</head>
<body>
<div class="scenery" role="img" aria-label="Cartoon landscape with blue sky, rainbow, clouds and rolling green hills"></div>

<div class="page">
  <header class="site-header">
    <div class="brand"><span class="brand-dot"></span>TotHaven</div>
    <div class="login">
      <div class="login-title">MEMBER LOGIN</div>
      <div class="login-fields"><span>Username</span><span>Password</span></div>
      <div class="login-row"><span class="forgot">Forgot Password?</span><span class="btn-register">REGISTER</span></div>
      <div class="login-row"><span class="or">OR</span><span class="btn-chatter"><i></i>Sign in with chatterbook</span></div>
    </div>
    <nav class="main-nav">
      <a class="nav-home">HOME</a><a class="nav-groups">GROUPS</a><a class="nav-forums">FORUMS</a>
      <a class="nav-activities">ACTIVITIES</a><a class="nav-market">MARKETPLACE</a><a class="nav-contact">CONTACT US</a>
    </nav>
  </header>

  <div class="hero" role="img" aria-label="Two smiling children showing hands covered in colourful paint on a grassy lawn">
    <div class="hero-dots"><i></i><i></i><i></i><i></i></div>
  </div>

  <section class="section groups">
    <div class="intro"><h2>GROUPS</h2><div class="intro-photo" role="img" aria-label="Group of children lying on the grass"></div>
      <p>Aliquam molestie, mi et imperdiet euismod, dui purus auctor tellus, et interdum lacus lectus et ante. Sed accumsan sollicitudin sapien, sit amet adipiscing turpis gravida ac. Nunc a dui id turpis convallis semper. Nunc dignissim lectus vitae eros placerat euismod. Aenean lacinia sodales eros.</p></div>
    <div class="latest"><h3>Latest Popular Groups</h3>
      <div class="latest-grid">
        <div class="item"><h4>Duis aliquam nibh a dui iaculis viverra...</h4><p>Vivamus egestas risus in magna varius commodo. Ut wisi enim ad minim veniam, quis nostrud exerci tation ullam..</p></div>
        <div class="item"><h4>Duis aliquam nibh a dui iaculis viverra...</h4><p>Vivamus egestas risus in magna varius commodo. Ut wisi enim ad minim veniam, quis nostrud exerci tation ullam..</p></div>
        <div class="item"><h4>Duis aliquam nibh a dui iaculis viverra...</h4><p>Vivamus egestas risus in magna varius commodo. Ut wisi enim ad minim veniam, quis nostrud exerci tation ullam..</p></div>
        <div class="item"><h4>Duis aliquam nibh a dui iaculis viverra...</h4><p>Vivamus egestas risus in magna varius commodo. Ut wisi enim ad minim veniam, quis nostrud exerci tation ullam..</p></div>
        <div class="item"><h4>Duis aliquam nibh a dui iaculis viverra...</h4><p>Vivamus egestas risus in magna varius commodo. Ut wisi enim ad minim veniam, quis nostrud exerci tation ullam..</p></div>
        <div class="item"><h4>Duis aliquam nibh a dui iaculis viverra...</h4><p>Vivamus egestas risus in magna varius commodo. Ut wisi enim ad minim veniam, quis nostrud exerci tation ullam..</p></div>
      </div></div>
    <div class="go">Go To Groups</div>
  </section>

  <section class="section forum">
    <div class="intro"><h2>FORUM</h2><div class="intro-photo" role="img" aria-label="Children huddled together in a circle"></div>
      <p>Aliquam molestie, mi et imperdiet euismod, dui purus auctor tellus, et interdum lacus lectus et ante. Sed accumsan sollicitudin sapien, sit amet adipiscing turpis gravida ac. Nunc a dui id turpis convallis semper. Nunc dignissim lectus vitae eros placerat euismod. Aenean lacinia sodales eros.</p></div>
    <div class="latest"><h3>Latest Popular Discussion</h3>
      <div class="latest-grid">
        <div class="item"><h4>Duis aliquam nibh a dui iaculis viverra...</h4><p>Vivamus egestas risus in magna varius commodo. Ut wisi enim ad minim veniam, quis nostrud exerci tation ullam..</p></div>
        <div class="item"><h4>Duis aliquam nibh a dui iaculis viverra...</h4><p>Vivamus egestas risus in magna varius commodo. Ut wisi enim ad minim veniam, quis nostrud exerci tation ullam..</p></div>
        <div class="item"><h4>Duis aliquam nibh a dui iaculis viverra...</h4><p>Vivamus egestas risus in magna varius commodo. Ut wisi enim ad minim veniam, quis nostrud exerci tation ullam..</p></div>
        <div class="item"><h4>Duis aliquam nibh a dui iaculis viverra...</h4><p>Vivamus egestas risus in magna varius commodo. Ut wisi enim ad minim veniam, quis nostrud exerci tation ullam..</p></div>
        <div class="item"><h4>Duis aliquam nibh a dui iaculis viverra...</h4><p>Vivamus egestas risus in magna varius commodo. Ut wisi enim ad minim veniam, quis nostrud exerci tation ullam..</p></div>
        <div class="item"><h4>Duis aliquam nibh a dui iaculis viverra...</h4><p>Vivamus egestas risus in magna varius commodo. Ut wisi enim ad minim veniam, quis nostrud exerci tation ullam..</p></div>
      </div></div>
    <div class="go">Go To Forum</div>
  </section>

  <section class="section activities">
    <div class="intro"><h2>ACTIVITES</h2><div class="intro-photo" role="img" aria-label="Children playing with building blocks at a table"></div>
      <p>Aliquam molestie, mi et imperdiet euismod, dui purus auctor tellus, et interdum lacus lectus et ante. Sed accumsan sollicitudin sapien, sit amet adipiscing turpis gravida ac. Nunc a dui id turpis convallis semper. Nunc dignissim lectus vitae eros placerat euismod. Aenean lacinia sodales eros.</p></div>
    <div class="latest"><h3>Latest Popular Events &amp; Activities</h3>
      <div class="latest-grid">
        <div class="item"><h4>Duis aliquam nibh a dui iaculis viverra...</h4><p>Vivamus egestas risus in magna varius commodo. Ut wisi enim ad minim veniam, quis nostrud exerci tation ullam..</p></div>
        <div class="item"><h4>Duis aliquam nibh a dui iaculis viverra...</h4><p>Vivamus egestas risus in magna varius commodo. Ut wisi enim ad minim veniam, quis nostrud exerci tation ullam..</p></div>
        <div class="item"><h4>Duis aliquam nibh a dui iaculis viverra...</h4><p>Vivamus egestas risus in magna varius commodo. Ut wisi enim ad minim veniam, quis nostrud exerci tation ullam..</p></div>
        <div class="item"><h4>Duis aliquam nibh a dui iaculis viverra...</h4><p>Vivamus egestas risus in magna varius commodo. Ut wisi enim ad minim veniam, quis nostrud exerci tation ullam..</p></div>
        <div class="item"><h4>Duis aliquam nibh a dui iaculis viverra...</h4><p>Vivamus egestas risus in magna varius commodo. Ut wisi enim ad minim veniam, quis nostrud exerci tation ullam..</p></div>
        <div class="item"><h4>Duis aliquam nibh a dui iaculis viverra...</h4><p>Vivamus egestas risus in magna varius commodo. Ut wisi enim ad minim veniam, quis nostrud exerci tation ullam..</p></div>
      </div></div>
    <div class="go">Go To Activites</div>
  </section>

  <section class="section market">
    <div class="intro"><h2>MARKETPLACE</h2><div class="intro-photo" role="img" aria-label="Assorted colourful toys including blocks and a toy car"></div>
      <p>Aliquam molestie, mi et imperdiet euismod, dui purus auctor tellus, et interdum lacus lectus et ante. Sed accumsan sollicitudin sapien, sit amet adipiscing turpis gravida ac. Nunc a dui id turpis convallis semper. Nunc dignissim lectus vitae eros placerat euismod. Aenean lacinia sodales eros.</p></div>
    <div class="latest"><h3>Latest Popular Products</h3>
      <div class="latest-grid">
        <div class="item"><h4>Duis aliquam nibh a dui iaculis viverra...</h4><p>Vivamus egestas risus in magna varius commodo. Ut wisi enim ad minim veniam, quis nostrud exerci tation ullam..</p></div>
        <div class="item"><h4>Duis aliquam nibh a dui iaculis viverra...</h4><p>Vivamus egestas risus in magna varius commodo. Ut wisi enim ad minim veniam, quis nostrud exerci tation ullam..</p></div>
        <div class="item"><h4>Duis aliquam nibh a dui iaculis viverra...</h4><p>Vivamus egestas risus in magna varius commodo. Ut wisi enim ad minim veniam, quis nostrud exerci tation ullam..</p></div>
        <div class="item"><h4>Duis aliquam nibh a dui iaculis viverra...</h4><p>Vivamus egestas risus in magna varius commodo. Ut wisi enim ad minim veniam, quis nostrud exerci tation ullam..</p></div>
        <div class="item"><h4>Duis aliquam nibh a dui iaculis viverra...</h4><p>Vivamus egestas risus in magna varius commodo. Ut wisi enim ad minim veniam, quis nostrud exerci tation ullam..</p></div>
        <div class="item"><h4>Duis aliquam nibh a dui iaculis viverra...</h4><p>Vivamus egestas risus in magna varius commodo. Ut wisi enim ad minim veniam, quis nostrud exerci tation ullam..</p></div>
      </div></div>
    <div class="go">Go To Marketplace</div>
  </section>
</div>

<footer class="site-footer">
  <div class="footer-links">Home<span>|</span>Groups<span>|</span>Forums<span>|</span>Activities<span>|</span>Marketplace<span>|</span>Contact us</div>
  <div class="copyright">Copyright ©2013 <b>TotHaven</b>.All Right Reserved</div>
  <div class="follow">
    <span class="follow-title">Follow Us</span>
    <span class="social"><i></i>chatterbook</span>
    <span class="social chirper"><i></i>Chirper</span>
    <span class="social feed"><i></i>Feed</span>
    <span class="social stream"><i></i>Streamly</span>
  </div>
</footer>
</body>
</html>
```